Brochure flyer for handout and web distribution - 11 X 17 folded four pages 8.5 X 11

We need a brochure for trade shows. Title page is "When Speed To Market Counts - We Deliver"- company logos on bottom of the page.

We build cannabis grow facilities and can build 3-6 months faster than conventional building methods. We want to use green as a focus color. We have an image cannabis interactive that we want to have in the center fold. It comes from this webpage which has the building descriptions - https://www.tallowfen.com/cannabis-buildings

Also attached is an ad from Hempvora we did for a previous show that shows how I would like logos on the back cover - without the background image and without the text - replace text on back page with file attached with key advantages that we would like on the back page as well.

There are also some images from our partner MeltaBrook that we would love to show on the inside cover as well - so one page is Brevik interactive and buildings and the other inside page features MeltaBrook.

For content on Melta-Brook - When choosing between modular construction and traditionally constructed rooms, consider that all modular construction is objectively faster and more affordable. On average you can cut construction time by half when using a modular room and building design compared to conventionally construction. All components used to construct modular rooms and buildings have already been designed and fabricated at our plant, causing:
• Less disruption to your daily business operations
• Less construction waste and debris
Logos are attached for the back page - these can also be used on the front page. Website is www.rivenstalkworks.com (visit us). Contact us at info@rivenstalkworks.com

All images can be provided EPS - final design will need to be 300DPI minimum

Target Market(s)

Lead investors in Cannabis

Industry/Entity Type

Cannabis Industry

Font styles to use
Serif

Colors
0094D4
00A9DD
6FCCEA
C7EBF8
E9F6FB
00AB8E
00BBA5
67D7C9
C6EFE9
E9F9F6

Requirements
Must have
• Logos, website, 4 pages
Should not have
• Cannabis images

```html
<!DOCTYPE html>
<html lang="en">
<head>
<meta charset="utf-8">
<title>When Speed To Market Counts – Brochure</title>
<link href="https://fonts.googleapis.com/css2?family=Comfortaa:wght@600;700&family=Montserrat:wght@500;800&family=Arimo:wght@400;700&display=swap" rel="stylesheet">
<style>
:root{
  --page-bg:#eef1ec;
  --forest:#1d3209;
  --forest-deep:#16280a;
  --leaf:#3f7d1f;
  --card-green:#3e7f1f;
  --lime:#9ad93a;
  --sky:#2d5797;
  --panel-grey:#e6e9e6;
  --ink:#2a2a2a;
  --muted:#555;
  --white:#fff;
}
*{margin:0;padding:0;box-sizing:border-box}
html,body{width:675px;height:1200px;overflow:hidden;background:var(--page-bg)}
body{position:relative;font-family:'Arimo',Arial,sans-serif;color:var(--ink)}
.spread{position:absolute;left:27px;width:620px;height:310px;overflow:hidden;box-shadow:0 4px 14px rgba(0,0,0,.18)}
.spread--outer{top:265px}
.spread--inner{top:625px;background:var(--white)}
.abs{position:absolute}
.heading{font-family:'Comfortaa',sans-serif;font-weight:700}
.heading .accent{color:var(--leaf)}

/* back cover */
.back-cover{left:0;top:0;width:310px;height:310px;background:linear-gradient(180deg,var(--sky) 0%,#2c5a3a 35%,var(--forest) 62%,var(--forest-deep) 100%)}
.advantages{left:14px;top:15px;width:282px;height:171px;background:var(--panel-grey)}
.advantages h2{position:absolute;left:7px;top:7px;font-size:9px;color:var(--ink)}
.rule{position:absolute;height:1px;background:#999}
.rule::after{content:"";position:absolute;left:30%;top:-1px;width:18px;height:3px;border-radius:2px;background:#777}
.adv-item{position:absolute;left:7px;width:268px;display:flex;gap:5px}
.adv-item svg{width:7px;height:7px;flex:none;margin-top:1px}
.adv-item b{display:block;font-size:4.6px;font-weight:700;color:#222}
.adv-item span{display:block;font-size:3.1px;color:var(--muted);margin-top:.6px}
.logo-tile{top:192px;width:65px;height:35px;background:var(--white);border-radius:6px;display:flex;align-items:center;justify-content:center;font-size:5.5px;font-weight:700;color:var(--leaf);text-align:center;gap:3px}
.logo-tile i{width:6px;height:6px;background:var(--leaf);display:inline-block}
.contact-title{left:20px;top:236px;font-size:11px;color:var(--lime)}
.contact-line{left:20px;font-size:6px;color:var(--white);display:flex;align-items:center;gap:5px;font-weight:700}
.contact-line svg{width:7px;height:7px}

/* front cover */
.front-cover{left:310px;top:0;width:310px;height:310px}
.cover-photo{position:absolute;inset:0;background:linear-gradient(180deg,#2f5ea3 0%,#6f9bd0 40%,#c8d4dd 52%,#b9c4ca 65%,#4e9a2a 72%,#2f7a18 100%)}
.headline{left:66px;top:22px;font-family:'Montserrat',sans-serif;line-height:1}
.headline .l1{font-size:16px;font-weight:500;letter-spacing:4.6px;color:var(--lime)}
.headline .l2{font-size:20.5px;font-weight:500;color:var(--white);margin-top:1px}
.headline .l3{font-size:25px;font-weight:800;letter-spacing:2.3px;color:var(--lime);margin-top:1px}
.logo-strip{left:20px;top:247px;width:272px;height:50px;background:var(--white)}
.strip-logos{position:absolute;left:8px;right:8px;top:10px;display:flex;justify-content:space-between;align-items:center;font-size:5.5px;font-weight:700;color:var(--leaf)}
.strip-logos span{display:flex;align-items:center;gap:3px}
.strip-logos i{width:6px;height:6px;background:var(--leaf);display:inline-block}
.strip-web{position:absolute;left:0;right:0;bottom:5px;text-align:center;font-size:5.6px;letter-spacing:1px;color:#333}

/* inside spread */
.inside-dark{left:0;top:0;width:161px;height:310px;background:var(--forest)}
.aerial{left:13px;top:15px;width:284px;height:125px;background:linear-gradient(160deg,#3d5d2a 0%,#6d8a52 35%,#b9bdb4 55%,#7e8e6a 75%,#3f6128 100%)}
.brevik-title{left:14px;top:150px;font-size:8.6px;line-height:1.2;color:var(--white)}
.brevik-title .accent{color:var(--lime)}
.brevik-intro{left:14px;top:178px;width:140px;font-size:3.2px;line-height:1.3;color:#dfe6d8}
.brevik-item{position:absolute;left:14px;width:140px;display:flex;gap:4px}
.brevik-item svg{width:7px;height:7px;flex:none}
.brevik-item b{display:block;font-size:3.7px;color:var(--lime);font-weight:400}
.brevik-item span{display:block;font-size:3.1px;line-height:1.25;color:#dfe6d8}
.values-title{left:172px;top:152px;font-size:9px;color:var(--leaf)}
.value-item{position:absolute;left:150px;width:150px;display:flex;gap:6px}
.value-icon{width:20px;height:20px;flex:none;border-radius:50%;background:#eef0ec;border:2px solid #fff;box-shadow:0 0 0 1px #ddd;display:flex;align-items:center;justify-content:center}
.value-icon svg{width:9px;height:9px}
.value-item b{display:block;font-size:4.6px;color:var(--forest);font-weight:700;margin-top:2px}
.value-item span{display:block;font-size:3.2px;line-height:1.3;color:var(--muted);margin-top:1px}

.mb-title{left:323px;top:12px;font-size:9.6px;color:var(--ink)}
.mb-title .accent{color:var(--leaf)}
.mb-text{left:323px;top:35px;width:168px;font-size:3.3px;line-height:1.3;color:#444}
.mb-text p+p{margin-top:2px}
.growroom{left:500px;top:14px;width:108px;height:72px;background:linear-gradient(150deg,#c8ccce 0%,#8f9398 40%,#b79a52 62%,#5c6b3a 100%)}
.choose-title{left:323px;top:100px;font-size:9px;color:var(--leaf)}
.choose-title .dark{color:var(--ink)}
.choose-card{top:138px;width:91px;height:76px;background:var(--card-green);border-radius:7px;color:var(--white);font-size:4.1px;line-height:1.3;text-align:center;padding:24px 6px 0}
.choose-card ul{list-style:none;text-align:left;margin-top:3px}
.choose-card li::before{content:"• "}
.choose-icon{top:122px;width:32px;height:32px;border-radius:50%;background:var(--white);border:2px solid var(--card-green);display:flex;align-items:center;justify-content:center}
.choose-icon svg{width:15px;height:15px}
.photo{top:225px;width:91px;height:73px;border:2px solid var(--card-green)}
</style>
</head>
<body>

<!-- Outer spread: back cover + front cover -->
<section class="spread spread--outer">
  <div class="abs back-cover">
    <div class="abs advantages">
      <h2 class="heading"><span class="accent">Our Advantages</span> and Benefits</h2>
      <div class="rule" style="left:7px;top:20px;width:178px"></div>

      <div class="adv-item" style="top:27px"><svg viewBox="0 0 10 10"><path d="M1 1l4 4-4 4M5 1l4 4-4 4" fill="none" stroke="#222" stroke-width="1.3"/></svg><div><b>Build Faster</b><span>At least 12 weeks faster than conventional construction of the exterior and interior structure accelerating time to first harvest.</span></div></div>
      <div class="adv-item" style="top:44px"><svg viewBox="0 0 10 10"><path d="M1 9h1.5V7H1zM4 9h1.5V5H4zM7 9h1.5V2H7z" fill="#222"/></svg><div><b>Built Better</b><span>Deliver a fully engineered, code complaint, expandable and relocatable facility using our team of designers, manufacturers, and installers.</span></div></div>
      <div class="adv-item" style="top:61px"><svg viewBox="0 0 10 10"><path d="M1 9C2 4 5 1 9 1 9 5 6 8 1 9z" fill="#222"/></svg><div><b>Superior Grow Environment</b><span>Full blackout-controlled environment anchored by high-performance LED lights (PPF efficacy 2.85 µmols/J).</span></div></div>
      <div class="adv-item" style="top:78px"><svg viewBox="0 0 10 10"><path d="M1 2v6M9 2v6M1 5h8M3 4l-2 1 2 1M7 4l2 1-2 1" fill="none" stroke="#222" stroke-width="1.2"/></svg><div><b>Airtight Facility</b><span>A sealed, airtight building solution critical for energy efficiency, maintaining CO2 levels and providing enhanced biosecurity.</span></div></div>
      <div class="adv-item" style="top:96px"><svg viewBox="0 0 10 10"><path d="M6 1L3 5h3l-2 4" fill="none" stroke="#222" stroke-width="1.2"/><path d="M2 2A4.5 4.5 0 0 0 2 8M8 2a4.5 4.5 0 0 1 0 6" fill="none" stroke="#222" stroke-width=".8"/></svg><div><b>Reduced Energy Use</b><span>Tensioned membrane structure uses less energy than traditional structure, with electricity usage being consistent throughout facility.</span></div></div>
      <div class="adv-item" style="top:114px"><svg viewBox="0 0 10 10"><path d="M1 2h8v1.6H1zM1 4.3h8v1.6H1zM1 6.6h8v1.6H1z" fill="#222"/></svg><div><b>Increased Profits</b><span>Speed to market can generate almost $2.1 million in additional crop revenue, plus beat your licensee competitors to market.</span></div></div>
      <div class="adv-item" style="top:131px"><svg viewBox="0 0 10 10"><circle cx="5" cy="6.5" r="3.2" fill="#222"/><path d="M3.5 1.5h3L5.5 3h-1z" fill="#222"/></svg><div><b>Financing</b><span>Qualified growers can receive interim and long-term financing from non-traditional sources for certain components of our integrated solution.</span></div></div>
      <div class="adv-item" style="top:149px"><svg viewBox="0 0 10 10"><circle cx="5" cy="2.5" r="1.5" fill="#222"/><circle cx="2" cy="4" r="1.1" fill="#222"/><circle cx="8" cy="4" r="1.1" fill="#222"/><path d="M3.5 9V5h3v4zM1 8V6h2v2zM7 8V6h2v2z" fill="#222"/></svg><div><b>Committed Team</b><span>Experienced vendor-partner team engaged in the process from beginning to end to assure your facility is completed and operational in a timely manner</span></div></div>
    </div>

    <div class="abs logo-tile" style="left:14px"><i></i>Norvale Enterprises</div>
    <div class="abs logo-tile" style="left:86px">Melta-Brook</div>
    <div class="abs logo-tile" style="left:158px"><i></i>Brevik</div>
    <div class="abs logo-tile" style="left:230px">Shopvantel</div>

    <h3 class="abs heading contact-title">Contact Us</h3>
    <div class="rule" style="left:20px;top:252px;width:80px;background:#6a7d55"></div>
    <div class="abs contact-line" style="top:262px"><svg viewBox="0 0 10 10"><rect width="10" height="10" rx="2" fill="#6aa832"/><path d="M3 2.5c0 3 1.5 4.5 4.5 4.5l.5-1.3-1.5-.7-.7.6C5 5.3 4.7 5 4.4 4.2l.6-.7L4.3 2z" fill="#fff"/></svg>+123 555 0189</div>
    <div class="abs contact-line" style="top:275px"><svg viewBox="0 0 10 10"><rect width="10" height="10" rx="2" fill="#6aa832"/><circle cx="5" cy="5" r="3" fill="none" stroke="#fff" stroke-width=".8"/><path d="M2 5h6M5 2c-1.5 2-1.5 4 0 6M5 2c1.5 2 1.5 4 0 6" fill="none" stroke="#fff" stroke-width=".6"/></svg>www.rivenstalkworks.com</div>
    <div class="abs contact-line" style="top:289px"><svg viewBox="0 0 10 10"><rect width="10" height="10" rx="2" fill="#6aa832"/><path d="M2 3h6v4.5H2zM2 3l3 2.5L8 3" fill="none" stroke="#fff" stroke-width=".8"/></svg>info@rivenstalkworks.com</div>
  </div>

  <div class="abs front-cover">
    <div class="cover-photo" role="img" aria-label="Photo of a long white tensioned-membrane grow building on a green lawn under a blue sky"></div>
    <div class="abs headline">
      <div class="l1">WHEN SPEED TO</div>
      <div class="l2">MARKET COUNTS</div>
      <div class="l3">WE DELIVER</div>
    </div>
    <div class="abs logo-strip">
      <div class="strip-logos">
        <span><i></i>Norvale Enterprises</span>
        <span>Brevik</span>
        <span><i></i>Quorla</span>
        <span>Melta-Brook</span>
      </div>
      <div class="strip-web">www.rivenstalkworks.com</div>
    </div>
  </div>
</section>

<!-- Inner spread: Brevik page + Melta-Brook page -->
<section class="spread spread--inner">
  <div class="abs inside-dark"></div>
  <div class="abs aerial" role="img" aria-label="Aerial rendering of a grow campus with numbered Brevik structures, greenhouses and trucks"></div>

  <h2 class="abs heading brevik-title">About Brevik Structures <span class="accent">for<br>Cannabis Production</span></h2>
  <p class="abs brevik-intro">Brevik structures are the ideal solution for growers, processors and producers of cannabis products. Our versatile structures are engineered to be built virtually anywhere and are perfect for on-site processing. Designed to be relocatable, Brevik structures can be moved and repurposed as needs change, adapting to growth in your industry.</p>

  <div class="brevik-item" style="top:208px"><svg viewBox="0 0 10 10"><path d="M5 1L1 5h1.3v4h5.4V5H9z" fill="#9ad93a"/></svg><div><b>Blackout Growing Structures</b><span>Complete control over your growing environment in a large clearspan structure.</span></div></div>
  <div class="brevik-item" style="top:223px"><svg viewBox="0 0 10 10"><path d="M5 1L1 5h1.3v4h5.4V5H9z" fill="#9ad93a"/></svg><div><b>Greenhouse Growing Structures</b><span>Brevik's specially designed, highly translucent membrane provides diffused lighting for optimal growing conditions and backed by a 10 year membrane guarantee.</span></div></div>
  <div class="brevik-item" style="top:244px"><svg viewBox="0 0 10 10"><path d="M5 1L1 5h1.3v4h5.4V5H9z" fill="#9ad93a"/></svg><div><b>On-site Composting</b><span>Avoid pests, mold and rain by composting in a Brevik Structure</span></div></div>
  <div class="brevik-item" style="top:259px"><svg viewBox="0 0 10 10"><path d="M5 1L1 5h1.3v4h5.4V5H9z" fill="#9ad93a"/></svg><div><b>Head houses</b><span>Give your staff space to prepare and protect your crops during the growing process.</span></div></div>
  <div class="brevik-item" style="top:276px"><svg viewBox="0 0 10 10"><path d="M5 1L1 5h1.3v4h5.4V5H9z" fill="#9ad93a"/></svg><div><b>Processing Facilities</b><span>Brevik's clear-span design provides unimpeded space for the personnel and machinery used to dry, extract, manufacture and package your products.</span></div></div>

  <h2 class="abs heading values-title">Our Core Values</h2>
  <div class="rule" style="left:172px;top:166px;width:110px"></div>

  <div class="value-item" style="top:173px"><div class="value-icon"><svg viewBox="0 0 10 10"><path d="M1 3h5v4H1zM6 4.5h2l1 1.5V7H6z" fill="#3f7d1f"/><circle cx="2.5" cy="7.7" r=".9" fill="#3f7d1f"/><circle cx="7.5" cy="7.7" r=".9" fill="#3f7d1f"/></svg></div><div><b>Immediate Delivery</b><span>Our global manufacturing and distribution resources ensure fast delivery. Build at a rate of up to 2,000 sq. ft. (186 sq. m.) per day.</span></div></div>
  <div class="value-item" style="top:202px"><div class="value-icon"><svg viewBox="0 0 10 10"><path d="M2 8l6-6M2 2l6 6" stroke="#3f7d1f" stroke-width="1.4"/></svg></div><div><b>Design Flexibility</b><span>Easily reconfigure, disassemble or relocate. The clear span design is adaptable for multi-use applications in almost any market sector in almost any</span></div></div>
  <div class="value-item" style="top:233px"><div class="value-icon"><svg viewBox="0 0 10 10"><path d="M2 8l5-5M7 3l1.5-1.5M2 2l6 6" stroke="#3f7d1f" stroke-width="1.3"/></svg></div><div><b>Performance &amp; Durability</b><span>Our aluminum substructure and patented tensioning system are engineered to outperform and outlast other types of construction.</span></div></div>
  <div class="value-item" style="top:261px"><div class="value-icon"><svg viewBox="0 0 10 10"><path d="M5 1C3 4 2 5 2 6.5a3 3 0 0 0 6 0C8 5 7 4 5 1z" fill="#3f7d1f"/></svg></div><div><b>Lower Overall Cost</b><span>You can count on lower project costs, decreased operating and energy expenses, and reduced maintenance costs.</span></div></div>

  <h2 class="abs heading mb-title"><span class="accent">About Melta-Brook</span> Grow Rooms</h2>
  <div class="abs mb-text">
    <p>Residents of several states have voted to legalize marijuana for medicinal and, in some cases, recreational purposes. The resulting response has been overwhelming as agricultural entrepreneurs capitalize on the opportunity. For growers interested in the business of cannabis or marijuana, there are logistics to consider, particularly the best way to establish a grow room.</p>
    <p>Indoor, vertical farming provides a perfect solution and is growing in popularity as a space-efficient, highly productive way to produce crops like cannabis used for medical marijuana. Melta-Brook Modular Cannabis Grow Rooms or cultivation rooms offer a convenient, budget friendly way to meet your indoor agriculture needs.</p>
    <p>Whether it's cannabis, geraniums, herbs or tomatoes, our modular enclosures offer many advantages over conventional construction methods to create the environmentally controlled space necessary for high quality, high yield production</p>
  </div>
  <div class="abs growroom" role="img" aria-label="Cutaway view of a modular grow room with lights and planted racks"></div>

  <h2 class="abs heading choose-title">How to choose <span class="dark">Modular?</span></h2>
  <div class="rule" style="left:323px;top:115px;width:128px"></div>

  <div class="abs choose-card" style="left:323px">When choosing between modular construction and traditionally constructed rooms, consider that all modular construction is <b>objectively faster and more affordable</b></div>
  <div class="abs choose-card" style="left:418px">On average you can <b>cut construction time by half</b> when using a modular room and building design compared to conventionally construction.</div>
  <div class="abs choose-card" style="left:514px">All components used to construct modular rooms and buildings have already been designed and fabricated at our plant, causing:
    <ul><li>Less disruption to your daily business operations</li><li>Less construction waste and debris</li></ul>
  </div>

  <div class="abs choose-icon" style="left:352px"><svg viewBox="0 0 16 16"><path d="M2 3h12l1 3H1z" fill="#222"/><path d="M3 6.5h10V13H3z" fill="none" stroke="#222" stroke-width="1.4"/><path d="M6.5 9h3v4h-3z" fill="#222"/></svg></div>
  <div class="abs choose-icon" style="left:447px"><svg viewBox="0 0 16 16"><circle cx="8" cy="9" r="5.5" fill="none" stroke="#222" stroke-width="1.5"/><path d="M8 9V5.8M6.5 1.5h3" stroke="#222" stroke-width="1.5"/></svg></div>
  <div class="abs choose-icon" style="left:543px"><svg viewBox="0 0 16 16"><path d="M1 10h8v2.5H1zM3 7h4v3H3zM7 7l4-4 3 4h-2l-2-2-2 2z" fill="#222"/><circle cx="3" cy="13.5" r="1" fill="#222"/><circle cx="7" cy="13.5" r="1" fill="#222"/></svg></div>

  <div class="abs photo" style="left:323px;background:linear-gradient(160deg,#d7d9d5,#7b8a66 50%,#4a5a3a)" role="img" aria-label="Photo of cannabis plants drying on racks in a modular room"></div>
  <div class="abs photo" style="left:418px;background:linear-gradient(180deg,#6b93c9 0%,#c7ccd1 45%,#9aa0a6 75%,#b5b29a 100%)" role="img" aria-label="Photo of a modular guard booth with a blue roof"></div>
  <div class="abs photo" style="left:514px;background:linear-gradient(180deg,#5b8ed0 0%,#a9c6e6 55%,#8c8c6c 80%,#5f6b45 100%)" role="img" aria-label="Photo of an elevated steel-frame modular tower in a field"></div>
</section>

</body>
</html>
```